Process Roadmap for Interior Design Firm

We are looking to ramp up the design appeal of our current process roadmap to be very visually interesting, while staying informative and descriptive about our process.

Target Market(s)

In-house Clients

Industry/Entity Type

Interior Design Firm focused on sustainable and holistic design.

Other font styles liked:
• raleway

Requirements
Must have
• 1.) it would be nice if the graphic provided a more clear indication of the “journey” from one step to the next, so that there was a clear sense of the progression (such that we are directing the viewer) 2.). We would want it to fit on an 8.5”x11” page (the page could be horizontal when we have the Calm Compass formatted out with the testimonials) (in addition to the testimonials, we may also want to have the detailed descriptions of each step of the process presented below the graphic, so that the graphic is cleaner) 3.) ideally the graphic is clear and simple enough to also be used on our Bi-Weekly Client Updates, which will be typed updates for clients re their project budgets, schedule and scope. The Calm Compass graphic (without all the testimonials) would be at the end of the update, and would fit on the page horizontally at the bottom, perhaps in a space which is 7.5”w x 4”h or so.
Should not have
• bold or bright colors. Natural neutrals are preferred, such as the ones featured on the provided graphic.

```html
<!DOCTYPE html>
<html lang="en">
<head>
<meta charset="utf-8">
<title>HRD Calm Compass</title>
<link rel="stylesheet" href="https://fonts.googleapis.com/css2?family=Montserrat:wght@400;500;700;900&family=Oswald:wght@500&family=Source+Sans+3:wght@300;400&display=swap">
<style>
  :root {
    --gold-deep: #bfae86;
    --gold-mid: #d9cba3;
    --gold-light: #e6dcbc;
    --title-gold: #cdb48b;
    --text-grey: #9c9c9c;
    --band: #e8e3d2;
    --card-top: #f7f8f9;
    --card-bottom: #d9e1e7;
    --card-edge: #ffffff;
    --trail: rgba(196, 209, 226, 0.75);
  }
  * { box-sizing: border-box; margin: 0; padding: 0; }
  html, body { width: 1200px; height: 959px; overflow: hidden; background: #ffffff; }
  .roadmap { position: relative; width: 1200px; height: 959px; background: #ffffff; overflow: hidden; font-family: "Source Sans 3", sans-serif; }

  .brand { position: absolute; left: 37px; top: 32px; display: flex; align-items: center; gap: 14px; }
  .brand-mark { width: 31px; height: 76px; background: var(--gold-light); }
  .brand-name { font-family: "Montserrat", sans-serif; font-weight: 400; color: var(--title-gold); font-size: 12px; letter-spacing: 2.5px; line-height: 1.6; text-transform: uppercase; }

  .page-title { position: absolute; left: 0; width: 1200px; top: 48px; text-align: center; font-family: "Montserrat", sans-serif; font-weight: 500; font-size: 58px; color: var(--title-gold); letter-spacing: 0.5px; padding-left: 10px; }

  .step { position: absolute; top: 260px; width: 150px; height: 340px; }
  .step-trail { position: absolute; left: -2px; top: 53px; width: 95px; height: 282px; background: linear-gradient(to right, var(--trail), rgba(255,255,255,0) 55%); transform: skewX(-3.5deg); transform-origin: top left; -webkit-mask-image: linear-gradient(to bottom, #000 20%, transparent); mask-image: linear-gradient(to bottom, #000 20%, transparent); }
  .step-icon { position: absolute; left: 0; top: 0; width: 65px; height: 53px; transform: skewX(-2deg); display: flex; align-items: center; justify-content: center; }
  .step-icon svg { width: 30px; height: 30px; transform: skewX(2deg); }
  .step-number { position: absolute; left: 10px; top: 52px; font-family: "Montserrat", sans-serif; font-weight: 900; font-size: 38px; letter-spacing: -1px; }
  .step-name { position: absolute; left: 16px; top: 105px; font-family: "Oswald", sans-serif; font-weight: 500; font-size: 16px; letter-spacing: 0.2px; }
  .step-text { position: absolute; left: 13px; top: 129px; width: 112px; font-weight: 300; font-size: 11px; line-height: 12.4px; color: var(--text-grey); }
  .step-text p + p { margin-top: 12px; }

  .tone-deep .step-icon { background: var(--gold-deep); }
  .tone-deep .step-number, .tone-deep .step-name { color: var(--gold-deep); }
  .tone-mid .step-icon { background: var(--gold-mid); }
  .tone-mid .step-number, .tone-mid .step-name { color: var(--gold-mid); }
  .tone-light .step-icon { background: var(--gold-light); }
  .tone-light .step-number, .tone-light .step-name { color: var(--gold-light); }

  .detail-band { position: absolute; left: 0; top: 634px; width: 1200px; height: 325px; background: var(--band); }
  .detail-card { position: absolute; top: 100px; width: 137px; height: 131px; border-radius: 9px; border: 1.5px solid var(--card-edge); background: linear-gradient(to bottom, var(--card-top), var(--card-bottom)); box-shadow: 0 6px 12px rgba(150, 150, 130, 0.25); text-align: center; padding: 16px 9px 0; }
  .detail-badge { position: absolute; left: 53px; top: -26px; width: 30px; height: 30px; border-radius: 50%; background: radial-gradient(circle at 40% 35%, #e4d7b2, #b9a675); border: 2px solid #f3eedf; color: #ffffff; font-family: "Montserrat", sans-serif; font-weight: 900; font-size: 14px; line-height: 26px; }
  .detail-title { font-family: "Montserrat", sans-serif; font-weight: 700; font-size: 12.5px; margin-bottom: 9px; }
  .detail-text { font-family: "Montserrat", sans-serif; font-size: 7.6px; line-height: 9.8px; color: #6f6f6f; }
  .detail-card.tone-deep .detail-title { color: var(--gold-deep); }
  .detail-card.tone-mid .detail-title { color: var(--gold-mid); }
  .detail-card.tone-light .detail-title { color: var(--gold-light); }
</style>
</head>
<body>
<main class="roadmap">
  <header>
    <div class="brand">
      <div class="brand-mark"></div>
      <div class="brand-name">Hollis Reed<br>Design</div>
    </div>
    <h1 class="page-title">HRD Calm Compass</h1>
  </header>

  <section class="steps">
    <article class="step tone-deep" style="left:77px">
      <div class="step-trail"></div>
      <div class="step-icon"><svg viewBox="0 0 24 24" fill="none" stroke="#fff" stroke-width="2.4" stroke-linecap="round"><path d="M4 16v-4a8 8 0 0 1 16 0v4"/><rect x="3" y="14" width="4" height="7" rx="1.5" fill="#fff"/><rect x="17" y="14" width="4" height="7" rx="1.5" fill="#fff"/></svg></div>
      <div class="step-number">01</div>
      <h2 class="step-name">LISTENING</h2>
      <div class="step-text"><p>Listening to our clients, their land, and their home.</p><p>Identifying their needs, challenges, wishes, and dreams.</p></div>
    </article>
    <article class="step tone-mid" style="left:236px">
      <div class="step-trail"></div>
      <div class="step-icon"><svg viewBox="0 0 24 24" fill="none" stroke="#fff" stroke-width="1.6" stroke-linecap="round"><path d="M3 13c3-4 6-5 9-5s6 1 9 5c-3 4-6 5-9 5s-6-1-9-5z"/><circle cx="12" cy="13" r="3"/><path d="M12 2v3M5 4l2 2M19 4l-2 2M4 21l2-2M20 21l-2-2"/></svg></div>
      <div class="step-number">02</div>
      <h2 class="step-name">VISIONING</h2>
      <div class="step-text"><p>Facilitating a guided visioning process to clarify the deepest intention, true purpose, and highest potential for their home and their future within it.</p></div>
    </article>
    <article class="step tone-light" style="left:395px">
      <div class="step-trail"></div>
      <div class="step-icon"><svg viewBox="0 0 24 24" fill="none" stroke="#fff" stroke-width="1.5" stroke-linecap="round"><rect x="4" y="2" width="14" height="20" rx="2"/><path d="M7 7l1 1 2-2M7 12l1 1 2-2M7 17l1 1 2-2M12 7h4M12 12h3M12 17h2"/><circle cx="18" cy="18" r="3" fill="#e6dcbc"/></svg></div>
      <div class="step-number">03</div>
      <h2 class="step-name">PLANNING</h2>
      <div class="step-text"><p>Turning our client's vision into a clearly defined scope., budget, and timeline.</p><p>Mapping out the steps for making their dream a reality.</p><p>Setting a meeting schedule from start to finish.</p></div>
    </article>
    <article class="step tone-deep" style="left:554px">
      <div class="step-trail"></div>
      <div class="step-icon"><svg viewBox="0 0 24 24" fill="none" stroke="#fff" stroke-width="1.6" stroke-linecap="round"><path d="M3 5h18"/><rect x="10" y="3" width="4" height="4" fill="#fff"/><circle cx="3" cy="5" r="1.5"/><circle cx="21" cy="5" r="1.5"/><path d="M7 10l5-3 5 3-3 7h-4z"/><path d="M12 7v6"/><rect x="9" y="18" width="6" height="3"/></svg></div>
      <div class="step-number">04</div>
      <h2 class="step-name">DESIGINING</h2>
      <div class="step-text"><p>Following the schedule through the design phases from initial design concepts, technical drawings and details, and the selection of all finishes, fixtures, and surnishings.</p></div>
    </article>
    <article class="step tone-mid" style="left:713px">
      <div class="step-trail"></div>
      <div class="step-icon"><svg viewBox="0 0 24 24" fill="none" stroke="#fff" stroke-width="1.6"><circle cx="12" cy="14" r="6" stroke-dasharray="3 2" stroke-width="3"/><circle cx="12" cy="5" r="2.2" fill="#fff"/><circle cx="6" cy="7" r="1.8" fill="#fff"/><circle cx="18" cy="7" r="1.8" fill="#fff"/><circle cx="12" cy="14" r="2.5" fill="#fff"/></svg></div>
      <div class="step-number">05</div>
      <h2 class="step-name">MANAGING</h2>
      <div class="step-text"><p>Coordinating with clients, builders, architects, and vendors to ensure that the design is executed with excellence, and the construction and furnishings are on-time and on-budget.</p></div>
    </article>
    <article class="step tone-light" style="left:872px">
      <div class="step-trail"></div>
      <div class="step-icon"><svg viewBox="0 0 24 24" fill="none" stroke="#fff" stroke-width="1.6" stroke-linecap="round"><circle cx="14" cy="7" r="3"/><circle cx="14" cy="7" r="5" stroke-dasharray="2 2.2" stroke-width="2.4"/><path d="M2 17l4-2c2-1 4 0 6 1h4M6 21l4-1h6l5-4"/></svg></div>
      <div class="step-number">06</div>
      <h2 class="step-name">INSTALLING</h2>
      <div class="step-text"><p>Overseeing the inspection, installation, and arrangement of all furnishings, lighting, artwork, and decorative items.</p><p>Taking care of every last detail.</p></div>
    </article>
    <article class="step tone-deep" style="left:1031px">
      <div class="step-trail"></div>
      <div class="step-icon"><svg viewBox="0 0 24 24" fill="none" stroke="#fff" stroke-width="2.2" stroke-linecap="round" stroke-linejoin="round"><path d="M20 10.5A8.5 8.5 0 1 1 15 4.2"/><path d="M8 12l4 4 9-10"/></svg></div>
      <div class="step-number">07</div>
      <h2 class="step-name">COMPLETING</h2>
      <div class="step-text"><p>Fixing any issues or defects.</p><p>Follow up on all remaining items.</p><p>Completing the final finishing touches to our client's full and total satisfaction.</p></div>
    </article>
  </section>

  <section class="detail-band">
    <div class="detail-card tone-deep" style="left:62px"><div class="detail-badge">1</div><h3 class="detail-title">TEXT TITLE</h3><p class="detail-text">Lorem ipsum dolor sit amet, consectetuer adipiscing elit, sed diam nonummy nibh euismod tincidunt ut laoreet dolore magna aliquam erat volutpat.</p></div>
    <div class="detail-card tone-mid" style="left:218px"><div class="detail-badge">2</div><h3 class="detail-title">TEXT TITLE</h3><p class="detail-text">Lorem ipsum dolor sit amet, consectetuer adipiscing elit, sed diam nonummy nibh euismod tincidunt ut laoreet dolore magna aliquam erat volutpat.</p></div>
    <div class="detail-card tone-light" style="left:375px"><div class="detail-badge">3</div><h3 class="detail-title">TEXT TITLE</h3><p class="detail-text">Lorem ipsum dolor sit amet, consectetuer adipiscing elit, sed diam nonummy nibh euismod tincidunt ut laoreet dolore magna aliquam erat volutpat.</p></div>
    <div class="detail-card tone-deep" style="left:531px"><div class="detail-badge">4</div><h3 class="detail-title">TEXT TITLE</h3><p class="detail-text">Lorem ipsum dolor sit amet, consectetuer adipiscing elit, sed diam nonummy nibh euismod tincidunt ut laoreet dolore magna aliquam erat volutpat.</p></div>
    <div class="detail-card tone-mid" style="left:688px"><div class="detail-badge">5</div><h3 class="detail-title">TEXT TITLE</h3><p class="detail-text">Lorem ipsum dolor sit amet, consectetuer adipiscing elit, sed diam nonummy nibh euismod tincidunt ut laoreet dolore magna aliquam erat volutpat.</p></div>
    <div class="detail-card tone-light" style="left:844px"><div class="detail-badge">6</div><h3 class="detail-title">TEXT TITLE</h3><p class="detail-text">Lorem ipsum dolor sit amet, consectetuer adipiscing elit, sed diam nonummy nibh euismod tincidunt ut laoreet dolore magna aliquam erat volutpat.</p></div>
    <div class="detail-card tone-deep" style="left:1001px"><div class="detail-badge">7</div><h3 class="detail-title">TEXT TITLE</h3><p class="detail-text">Lorem ipsum dolor sit amet, consectetuer adipiscing elit, sed diam nonummy nibh euismod tincidunt ut laoreet dolore magna aliquam erat volutpat.</p></div>
  </section>
</main>
</body>
</html>
```